New business card for civil engineering company - "Keystone Audit"

We need a business card designed for our new structural engineering company.

The company name is "Keystone Audit" logo files attached.

We would like the following:
* Two-sided card
* Simple design

Information to be placed on the card:
Name - Marcus Dellow
Job Title - Director / Structural Engineer
Credentials - BEng(Hons), CPEng, CMengNZ, IntPE(NZ)
Email - marcus.dellow@keystoneaudit.co.nz
mobile - 0219364058
website - www.keystoneaudit.co.nz

```html
<!DOCTYPE html>
<html lang="en">
<head>
<meta charset="utf-8">
<title>Keystone Audit – Business Card</title>
<link rel="stylesheet" href="https://fonts.googleapis.com/css2?family=Saira+Semi+Condensed:wght@400;500;600;700&display=swap">
<style>
  :root {
    --page-bg: #d3e9f7;
    --navy-deep: #2a3a66;
    --navy-mid: #35487f;
    --panel-blue: #465da3;
    --back-center: #3e5698;
    --back-edge: #2a3a66;
    --accent-blue: #5b9bd5;
    --icon-blue: #6cb6e8;
    --rule-soft: #6e84c2;
    --text-white: #ffffff;
    --text-soft: #e6ebf7;
  }
  * { margin: 0; padding: 0; box-sizing: border-box; }
  html, body {
    width: 1022px;
    height: 1200px;
    overflow: hidden;
    background: var(--page-bg);
    font-family: "Saira Semi Condensed", "Arial Narrow", "Liberation Sans Narrow", sans-serif;
  }
  .canvas { position: relative; width: 1022px; height: 1200px; }

  .card {
    position: absolute;
    left: 44px;
    width: 934px;
    height: 533px;
    overflow: hidden;
  }
  .card--front { top: 44px; background: var(--panel-blue); }
  .card--back {
    top: 622px;
    background: radial-gradient(ellipse 70% 75% at 50% 50%, var(--back-center) 0%, var(--navy-mid) 55%, var(--back-edge) 100%);
    display: flex;
    align-items: center;
    justify-content: center;
  }

  .identity {
    position: absolute;
    left: 0; top: 0;
    width: 413px;
    height: 100%;
    background: linear-gradient(135deg, var(--navy-deep) 0%, var(--navy-mid) 60%, #32467c 100%);
  }
  .identity__role {
    position: absolute;
    left: 48px; top: 136px;
    font-size: 14px;
    font-weight: 400;
    color: var(--text-soft);
    letter-spacing: 0.2px;
    white-space: nowrap;
  }
  .identity__name {
    position: absolute;
    left: 44px; top: 162px;
    max-width: 360px;
    font-size: 40px;
    font-weight: 600;
    line-height: 1.15;
    color: var(--text-white);
    white-space: nowrap;
  }
  .identity__rule {
    position: absolute;
    left: 44px; top: 232px;
    width: 133px; height: 4px;
    background: var(--accent-blue);
  }

  .contact {
    position: absolute;
    left: 475px; top: 165px;
    color: var(--text-white);
  }
  .contact__credentials {
    font-size: 20px;
    font-weight: 500;
    line-height: 28px;
    white-space: nowrap;
  }
  .contact__rule {
    width: 89px; height: 2px;
    margin-top: 20px;
    background: var(--rule-soft);
  }
  .contact__list { list-style: none; margin-top: 24px; }
  .contact__item {
    display: flex;
    align-items: center;
    height: 28px;
    margin-bottom: 20px;
    font-size: 20px;
    font-weight: 400;
    white-space: nowrap;
  }
  .contact__item--phone { font-weight: 600; }
  .contact__icon {
    width: 18px; height: 18px;
    margin-right: 12px;
    fill: var(--icon-blue);
    flex: none;
  }

  .brand-name {
    font-size: 40px;
    font-weight: 600;
    color: var(--text-white);
    letter-spacing: 4px;
    text-transform: uppercase;
  }
</style>
</head>
<body>
<main class="canvas">

  <section class="card card--front" aria-label="Card front">
    <div class="identity">
      <p class="identity__role">DIRECTOR / STRUCTURAL ENGINEER</p>
      <h1 class="identity__name">MARCUS DELLOW</h1>
      <div class="identity__rule"></div>
    </div>

    <div class="contact">
      <p class="contact__credentials">BEng(Hons), CPEng, CMengNZ, IntPE(NZ)</p>
      <div class="contact__rule"></div>
      <ul class="contact__list">
        <li class="contact__item">
          <svg class="contact__icon" viewBox="0 0 20 20" aria-hidden="true">
            <path d="M1 4h18v1.6l-9 5.4-9-5.4z"/>
            <path d="M1 7.6l9 5.4 9-5.4V16H1z"/>
          </svg>
          marcus.dellow@keystoneaudit.co.nz
        </li>
        <li class="contact__item contact__item--phone">
          <svg class="contact__icon" viewBox="0 0 20 20" aria-hidden="true">
            <path d="M4.2 1.5l3 3.4-1.7 2.3c1.2 2.6 3 4.5 5.6 5.8l2.3-1.7 3.4 3-1.6 3.1C8.4 16.9 3.1 11.6 1.6 3.1z"/>
          </svg>
          0219364058
        </li>
        <li class="contact__item">
          <svg class="contact__icon" viewBox="0 0 20 20" aria-hidden="true">
            <circle cx="10" cy="10" r="8.5"/>
            <path d="M6 5.5c1.5 0 2.5 1 2 2.2-.6 1.2-2.2 1-2.4 2.6-.2 1.2 1 1.8.8 3.2M12 4.5c.3 1.4 1.8 1.6 2.8 1.2M13.5 11c-1.2.2-1.6 1.5-.8 2.6.6.8.2 1.8-.3 2.6" stroke="#465da3" stroke-width="1.4" fill="none"/>
          </svg>
          www.keystoneaudit.co.nz
        </li>
      </ul>
    </div>
  </section>

  <section class="card card--back" aria-label="Card back">
    <p class="brand-name">Keystone Audit</p>
  </section>

</main>
</body>
</html>
```